KRV Business Cards

We are a local commercial development company based in Silicon Valley and we would like a new business card. I've attached a copy of our company brochure to give a flavor of what we do, our logo, info company colors/graphics, and our current business card. We don't necessarily need a crazy makeover, but would like something that feels a little bit more "fresh" and modern (we've had the same business card design for 15+ years), but still in keeping with our overall brand -- clean, high-quality, modern but timeless. Would like to add our website to the info on the card (www.lumbrel.com) and would like the flexibility for some folks to have an efax number listed and some not to have that included (without it looking like there is a hole).

```html
<!DOCTYPE html>
<html lang="en">
<head>
<meta charset="utf-8">
<title>KRV Business Cards</title>
<link href="https://fonts.googleapis.com/css2?family=Lato:wght@400;700&display=swap" rel="stylesheet">
<style>
  :root {
    --bg: #e9e7e3;
    --brand-blue: #41607f;
    --brand-blue-light: #5a7896;
    --brand-blue-dark: #34506c;
    --paper: #f4f4f2;
    --ink-light: #ffffff;
    --rule: rgba(255,255,255,0.55);
  }
  * { margin: 0; padding: 0; box-sizing: border-box; }
  html, body { width: 1200px; height: 942px; overflow: hidden; background: var(--bg); }
  .canvas { position: relative; width: 1200px; height: 942px; font-family: "Lato", sans-serif; }

  .card {
    position: absolute; left: 320px; width: 560px; height: 320px;
    box-shadow: 0 6px 18px rgba(0,0,0,0.18); overflow: hidden;
  }
  .card--front { top: 110px; background: var(--paper); }
  .card--back {
    top: 512px;
    background: radial-gradient(ellipse at 35% 30%, var(--brand-blue-light), var(--brand-blue) 55%, var(--brand-blue-dark));
  }

  /* front */
  .band { position: absolute; inset: 0; }
  .company-tab {
    position: absolute; left: 22px; top: 14px; width: 183px; height: 64px;
    display: flex; align-items: center; justify-content: center;
    color: var(--ink-light); font-size: 12px; font-weight: 400;
    line-height: 1.3; letter-spacing: 0.08em; text-align: center;
  }
  .holder { position: absolute; left: 40px; top: 122px; color: var(--ink-light); }
  .holder__name { font-weight: 700; font-size: 25px; letter-spacing: 0.02em; }
  .holder__title { font-size: 15px; letter-spacing: 0.05em; margin-top: 2px; }

  .contacts { position: absolute; left: 320px; top: 104px; width: 218px; list-style: none; color: var(--ink-light); }
  .contacts li {
    display: flex; align-items: center; gap: 10px; height: 29px;
    border-bottom: 1px solid var(--rule); font-size: 16px;
  }
  .contacts svg { width: 15px; height: 15px; flex: none; }

  .address {
    position: absolute; left: 40px; top: 270px; color: var(--brand-blue);
    font-size: 16px; letter-spacing: 0.01em;
  }

  /* back */
  .back-name {
    position: absolute; left: 160px; top: 88px; width: 300px;
    color: var(--ink-light); font-size: 26px; font-weight: 400;
    line-height: 1.15; letter-spacing: 0.06em; text-transform: uppercase;
  }
  .back-url {
    position: absolute; left: 162px; top: 236px;
    color: rgba(255,255,255,0.8); font-size: 14px; letter-spacing: 0.32em;
  }
</style>
</head>
<body>
<main class="canvas">

  <section class="card card--front">
    <svg class="band" viewBox="0 0 560 320" width="560" height="320">
      <defs>
        <linearGradient id="band-fill" x1="0" y1="0" x2="1" y2="1">
          <stop offset="0" stop-color="#4a6888"/>
          <stop offset="0.5" stop-color="#587694"/>
          <stop offset="1" stop-color="#3c5a79"/>
        </linearGradient>
      </defs>
      <path d="M0 78 H22 V14 H205 V78 H560 V240 H258 L246 254 L234 240 H0 Z" fill="url(#band-fill)"/>
      <g fill="#fff" transform="translate(240 226)">
        <path d="M6 0 a6 6 0 0 1 6 6 c0 4.5 -6 11 -6 11 s-6 -6.5 -6 -11 a6 6 0 0 1 6 -6z"/>
        <circle cx="6" cy="6" r="2.2" fill="#4a6888"/>
      </g>
    </svg>

    <p class="company-tab">KRV DEVELOPMENT<br>COMPANY, LLC</p>

    <div class="holder">
      <p class="holder__name">NORA J. CASTELL</p>
      <p class="holder__title">PARTNER</p>
    </div>

    <ul class="contacts">
      <li>
        <svg viewBox="0 0 16 16" aria-hidden="true"><path fill="#fff" d="M3.5 1 L6 4 L4.6 5.8 C5.5 7.8 8 10.3 10.2 11.4 L12 10 L15 12.5 L13.2 15 C7 14.5 1.5 9 1 2.8 Z"/></svg>
        650.555.0142
      </li>
      <li>
        <svg viewBox="0 0 16 16" aria-hidden="true"><rect x="4" y="1" width="8" height="14" rx="1.5" fill="none" stroke="#fff" stroke-width="1.4"/><circle cx="8" cy="12.5" r="0.9" fill="#fff"/></svg>
        650.555.0187
      </li>
      <li>
        <svg viewBox="0 0 16 16" aria-hidden="true"><rect x="4" y="1" width="8" height="5" fill="none" stroke="#fff" stroke-width="1.2"/><rect x="1" y="6" width="14" height="8" rx="1" fill="#fff"/><rect x="4" y="9" width="8" height="1.2" fill="#4a6888"/></svg>
        650.555.0319
      </li>
      <li>
        <svg viewBox="0 0 16 16" aria-hidden="true"><rect x="1" y="3" width="14" height="10" fill="#fff"/><path d="M1 3 L8 9 L15 3" fill="none" stroke="#4a6888" stroke-width="1.2"/></svg>
        nora@lumbrel.com
      </li>
    </ul>

    <p class="address">318 Linden Street, Palo Alto, California 94301</p>
  </section>

  <section class="card card--back">
    <p class="back-name">KRV Development<br>Company, LLC</p>
    <p class="back-url">lumbrel.com</p>
  </section>

</main>
</body>
</html>
```